International horse riding portal needs web design

We are looking for the web design for the new "Vosmerik" web portal.

Offers from the world of horses and riding should be found on this portal, eg from the categories riding schools, riding holidays, farriers, riding stables, riding stables. And all information about riding.

It is important that the different areas can be found easily and clearly. For some categories, some features should already be available in the search bar.

In addition, the design should make you want to go horse riding. The user should be emotionally picked up on the landing page.

In the lower area, some offers should be advertised, eg from the areas of riding holidays, riding training, and horse trading.

Please use the colors from the logo for the design.
C100 M50 Y10 K50 and C0 M20 Y60 K30

```html
<!DOCTYPE html>
<html lang="en">
<head>
<meta charset="utf-8">
<title>Vosmerik – Horse Riding Portal</title>
<link href="https://fonts.googleapis.com/css2?family=Playfair+Display&family=Poppins:wght@400;500;600&family=Roboto:wght@400;500&display=swap" rel="stylesheet">
<style>
:root{
  --navy:#003f6b;
  --navy-deep:#042d4f;
  --gold:#c79c5b;
  --white:#ffffff;
  --ink:#1d1d1d;
  --grey:#f1f1f1;
}
*{margin:0;padding:0;box-sizing:border-box}
html,body{width:673px;height:1200px;overflow:hidden;background:var(--white)}
body{position:relative;font-family:'Roboto',sans-serif;color:var(--ink)}
.abs{position:absolute}
.caps{font-family:'Poppins',sans-serif;text-transform:uppercase;letter-spacing:.22em}
.serif{font-family:'Playfair Display',serif;font-weight:400}

/* header */
.site-header{left:0;top:0;width:673px;height:93px;background:var(--white)}
.brand{left:78px;top:14px;width:66px;text-align:center}
.brand-mark{width:20px;height:20px;border-radius:50%;background:var(--gold);margin:0 auto 3px}
.brand-name{font-family:'Playfair Display',serif;font-size:11px;color:var(--navy);letter-spacing:.02em}
.search{left:151px;top:16px;width:175px;height:21px;border-radius:11px;background:var(--grey);font-size:4.3px;padding-left:11px;line-height:21px;font-weight:600;white-space:nowrap}
.search svg{position:absolute;right:9px;top:7px}
.nav{top:23px;font-size:5px;color:var(--ink);display:flex;gap:15px;left:359px;white-space:nowrap}
.nav .login::before{content:"";display:inline-block;width:5px;height:5px;border-radius:50%;background:var(--gold);margin-right:3px;vertical-align:-1px}
.cat-row{top:52px;left:0;width:673px;height:41px}
.cat{position:absolute;top:0;width:50px;margin-left:-25px;text-align:center}
.cat-icon{display:block;width:20px;height:20px;border-radius:50%;background:var(--gold);margin:0 auto 4px}
.cat-line{display:block;font-size:5px;line-height:6px;white-space:nowrap;color:var(--ink);letter-spacing:.2em}
.ring-arrow{width:11px;height:11px;border-radius:50%;border:.6px solid #999;display:flex;align-items:center;justify-content:center}

/* hero */
.hero{left:0;top:93px;width:673px;height:264px;background:radial-gradient(ellipse at 60% 45%,#5b5a4a 0%,#2a2f22 40%,#141a12 100%)}
.slides{left:78px;top:183px;color:#cfd3cc;font-size:5.5px;font-family:'Poppins',sans-serif}
.slides .num{position:absolute;left:0}
.slides .cur{color:#fff;font-weight:600;font-size:8px}
.slides .bar{position:absolute;left:4px;top:12px;width:.6px;height:32px;background:#ccc}
.tabs{left:185px;top:235px;display:flex;align-items:center}
.tab{font-size:4.7px;color:#fff;padding:0 7px;height:20px;line-height:20px;white-space:nowrap}
.tab.active{background:#fff;color:var(--ink);border-radius:6px 6px 0 0;width:71px;padding:0 0 0 16px}
.field{top:256px;height:20px;background:#fff;font-size:4.3px;font-weight:600;line-height:20px;padding-left:15px;white-space:nowrap}
.go{left:467px;top:256px;width:21px;height:21px;border-radius:50%;background:var(--gold);display:flex;align-items:center;justify-content:center}
.scroll-line{left:606px;top:126px;width:.6px;height:170px;background:#aaa}
.scroll-dot{left:604px;top:124px;width:4px;height:4px;border-radius:50%;background:#aaa}
.scroll-pill{left:595px;top:294px;width:23px;height:83px;border-radius:12px;background:var(--navy);color:#fff;font-size:4.6px;writing-mode:vertical-rl;transform:rotate(180deg);display:flex;align-items:center;justify-content:center;white-space:nowrap}
.social-rail{left:657px;top:210px;width:20px;height:60px;border-radius:10px 0 0 10px;background:var(--gold);display:flex;flex-direction:column;align-items:center;justify-content:space-evenly;padding:4px 0}
.social-rail i{width:3px;height:3px;border-radius:50%;background:#fff}

/* about */
.about{left:0;top:357px;width:673px;height:183px;background:var(--navy)}
.about-panel{left:60px;top:357px;width:613px;height:183px;background:var(--gold);border-top-left-radius:62px}
.about-photo{left:61px;top:408px;width:210px;height:132px;border-radius:105px 105px 0 0;background:radial-gradient(ellipse at 55% 40%,#6a6a60,#2b2f25 55%,#151a12)}
.about-dot{left:86px;top:414px;width:40px;height:40px;border-radius:50%;background:var(--navy);border:4px solid var(--gold)}
.about-title{left:290px;top:380px;width:360px;font-size:19px;line-height:20px;color:var(--navy-deep)}
.about-text{left:290px;top:430px;width:275px;font-size:5.3px;line-height:10px;color:#1b1b1b}
.btn{background:var(--navy);color:#fff;border-radius:10px;font-size:5px;text-align:center}
.know{left:290px;top:493px;width:66px;height:20px;line-height:20px;white-space:nowrap}

/* categories strip */
.strip{left:0;top:540px;width:673px;height:182px;background:var(--navy)}
.tile{top:571px;width:107px;height:101px;border-radius:6px}
.tile-label{top:687px;width:107px;text-align:center;color:#fff;font-size:6.5px;font-weight:600;white-space:nowrap}
.strip-arrow{width:16px;height:16px;border-radius:50%;border:.7px solid #bcd;display:flex;align-items:center;justify-content:center}

/* offers */
.offers-title{left:0;top:745px;width:673px;text-align:center;font-size:19px;line-height:20px;color:var(--ink)}
.offer{top:806px;width:146px}
.offer-img{width:146px;height:128px;border-radius:3px}
.offer h3{font-size:7px;font-weight:500;margin:12px 0 0 12px;color:var(--ink);white-space:nowrap}
.meta{display:flex;align-items:center;gap:4px;margin:5px 0 0 12px;font-size:3.8px;white-space:nowrap}
.meta .flag{width:11px;height:11px;border-radius:50%;background:linear-gradient(#b22 0 50%,#2b4a8a 50%)}
.meta .pin{width:11px;height:11px;border-radius:50%;background:var(--gold);display:flex;align-items:center;justify-content:center}
.offer p{font-size:5.3px;line-height:10px;margin:7px 0 0 12px;width:128px}
.more{margin:3px 0 0 12px;width:24px;height:9px;border-radius:5px;background:var(--navy);display:flex;align-items:center;justify-content:center;gap:1.5px}
.more i{width:2px;height:2px;border-radius:50%;background:#fff}
.ring-lg{width:16px;height:16px;border-radius:50%;border:.7px solid #333;display:flex;align-items:center;justify-content:center}

/* footer */
.footer{left:0;top:1050px;width:673px;height:150px;background:var(--navy-deep);color:#fff}
.contact-ico{width:34px;height:34px;border-radius:50%;background:var(--navy);display:flex;align-items:center;justify-content:center}
.contact-text{font-size:5.7px;line-height:8.5px;white-space:nowrap}
.vline{width:.6px;height:78px;background:#3b6fb5;top:0}
.vdot{width:4px;height:4px;border-radius:50%;background:#3b6fb5;top:77px}
.fsoc{width:15px;height:15px;border-radius:50%;background:var(--gold);top:93px}
.fnav{top:116px;left:0;width:673px;display:flex;justify-content:center;gap:17px;font-size:5.5px;font-weight:500;white-space:nowrap}
.copy{top:132px;left:0;width:673px;text-align:center;font-size:4.8px;letter-spacing:.1em}
</style>
</head>
<body>

<!-- header -->
<header class="abs site-header">
  <div class="abs brand"><div class="brand-mark"></div><div class="brand-name">VOSMERIK</div></div>
  <div class="abs search caps">Search features here
    <svg width="6" height="6" viewBox="0 0 10 10"><circle cx="4" cy="4" r="3" fill="none" stroke="#333" stroke-width="1.4"/><line x1="6.3" y1="6.3" x2="9" y2="9" stroke="#333" stroke-width="1.4"/></svg>
  </div>
  <nav class="abs nav caps"><span>Home</span><span>Services</span><span>About us</span><span>Contact</span><span class="login">Login / Register</span></nav>

  <div class="abs cat-row caps">
    <div class="abs ring-arrow" style="left:64px;top:11px"><svg width="5" height="5" viewBox="0 0 10 10"><path d="M9 5H1M4 2L1 5l3 3" stroke="#777" fill="none"/></svg></div>
    <div class="cat" style="left:104px"><span class="cat-icon"></span><span class="cat-line">Riding</span><span class="cat-line">schools</span></div>
    <div class="cat" style="left:154px"><span class="cat-icon"></span><span class="cat-line">Riding</span><span class="cat-line">holidays</span></div>
    <div class="cat" style="left:205px"><span class="cat-icon"></span><span class="cat-line" style="padding-top:3px">Farriers</span></div>
    <div class="cat" style="left:254px"><span class="cat-icon"></span><span class="cat-line">Riding</span><span class="cat-line">stables</span></div>
    <div class="cat" style="left:304px"><span class="cat-icon"></span><span class="cat-line">Category</span><span class="cat-line">5</span></div>
    <div class="cat" style="left:356px"><span class="cat-icon"></span><span class="cat-line">Category</span><span class="cat-line">6</span></div>
    <div class="cat" style="left:409px"><span class="cat-icon"></span><span class="cat-line">Category</span><span class="cat-line">7</span></div>
    <div class="cat" style="left:461px"><span class="cat-icon"></span><span class="cat-line">Category</span><span class="cat-line">8</span></div>
    <div class="cat" style="left:514px"><span class="cat-icon"></span><span class="cat-line">Category</span><span class="cat-line">9</span></div>
    <div class="cat" style="left:566px"><span class="cat-icon"></span><span class="cat-line">Category</span><span class="cat-line">10</span></div>
    <div class="abs ring-arrow" style="left:596px;top:11px"><svg width="5" height="5" viewBox="0 0 10 10"><path d="M1 5h8M6 2l3 3-3 3" stroke="#777" fill="none"/></svg></div>
  </div>
</header>

<!-- hero -->
<div class="abs hero" role="img" aria-label="Rider in a white shirt on a white horse in a dark meadow"></div>
<div class="abs slides">
  <span class="num cur" style="top:0">01</span><span class="bar"></span>
  <span class="num" style="top:47px">02</span>
  <span class="num" style="top:67px">03</span>
  <span class="num" style="top:88px">04</span>
  <span class="num" style="top:108px">05</span>
</div>
<div class="abs tabs caps">
  <div class="tab active">Category 1</div><div class="tab">Category 2</div><div class="tab">Category 3</div><div class="tab">Category 4</div><div class="tab">Category 5</div>
</div>
<div class="abs field caps" style="left:185px;width:172px">Select features
  <svg style="position:absolute;right:10px;top:8px" width="4" height="3" viewBox="0 0 8 5"><path d="M1 1l3 3 3-3" stroke="#333" fill="none"/></svg></div>
<div class="abs field caps" style="left:360px;width:104px">Zip / City</div>
<div class="abs go"><svg width="5" height="5" viewBox="0 0 10 10"><circle cx="4" cy="4" r="3" fill="none" stroke="#333" stroke-width="1.6"/><line x1="6.3" y1="6.3" x2="9" y2="9" stroke="#333" stroke-width="1.6"/></svg></div>
<div class="abs scroll-line"></div><div class="abs scroll-dot"></div>
<div class="abs scroll-pill caps">Scroll down</div>
<div class="abs social-rail"><i></i><i></i><i></i><i></i></div>

<!-- about -->
<section>
  <div class="abs about"></div>
  <div class="abs about-panel"></div>
  <div class="abs about-photo" role="img" aria-label="Rider on a white horse against a dark background"></div>
  <div class="abs about-dot"></div>
  <h1 class="abs serif about-title">Ihic tectio blab incienis aut hiliquo quisqui aeprectur? Uresequod qui ditis</h1>
  <p class="abs about-text">Lorem ipsum dolor sit amet, consectetur adipiscing elit. Id et odio viverra at sed tincidunt sem. Lacus suspendisse nisl bibendum felis imperdiet egestas ac lacinia. Pharetra eu hendrerit egestas facilisi. Tristique varius neque fringilla neque turpis purus. Auctor pulvinar metus venenatis purus tincidunt volutpat etiam. Sapien massa ullamcorper morbi porttitor auctor tincidunt. Et dui a scelerisque gravida fames vitae urna commodo. Et mauris sit massa a, quisque pharetra.</p>
  <div class="abs btn know caps">Know more</div>
</section>

<!-- categories strip -->
<section>
  <div class="abs strip"></div>
  <div class="abs strip-arrow" style="left:78px;top:593px"><svg width="6" height="6" viewBox="0 0 10 10"><path d="M9 5H1M4 2L1 5l3 3" stroke="#fff" fill="none"/></svg></div>
  <div class="abs" style="left:86px;top:609px;width:.6px;height:24px;background:#bcd"></div>
  <div class="abs strip-arrow" style="left:78px;top:633px"><svg width="6" height="6" viewBox="0 0 10 10"><path d="M1 5h8M6 2l3 3-3 3" stroke="#fff" fill="none"/></svg></div>
  <div class="abs tile" style="left:106px;background:linear-gradient(135deg,#6b4a2e,#a8652f 55%,#d9d2c4)" role="img" aria-label="Chestnut horse looking out of a stable box"></div>
  <div class="abs tile" style="left:232px;background:linear-gradient(#8a969c,#dfe3e0 35%,#b5c84a 55%,#7f9d1e)" role="img" aria-label="Dark horse walking on a green meadow"></div>
  <div class="abs tile" style="left:358px;background:linear-gradient(#2f5a86,#6a8fb0 50%,#b9a58c)" role="img" aria-label="Rider on a horse along the seashore"></div>
  <div class="abs tile" style="left:485px;background:linear-gradient(#8aa6b2,#b7aa95 60%,#8e7a62)" role="img" aria-label="Two men standing with a dark horse"></div>
  <div class="abs tile" style="left:611px;width:70px;background:linear-gradient(135deg,#d9cfc4,#8b4a28 55%,#5a3420)" role="img" aria-label="Bay horse with bridle"></div>
  <div class="abs tile-label caps" style="left:106px">Category 1</div>
  <div class="abs tile-label caps" style="left:232px">Category 2</div>
  <div class="abs tile-label caps" style="left:358px">Category 3</div>
  <div class="abs tile-label caps" style="left:485px">Category 4</div>
  <div class="abs tile-label caps" style="left:638px;text-align:left;width:40px;overflow:hidden">Category 5</div>
</section>

<!-- offers -->
<section>
  <h2 class="abs serif offers-title">Ihic tectio blab incienis aut hiliquo<br>quisqui aeprectur? Uresequod qui ditis</h2>
  <div class="abs ring-lg" style="left:79px;top:870px"><svg width="6" height="6" viewBox="0 0 10 10"><path d="M9 5H1M4 2L1 5l3 3" stroke="#333" fill="none"/></svg></div>
  <div class="abs ring-lg" style="left:577px;top:870px"><svg width="6" height="6" viewBox="0 0 10 10"><path d="M1 5h8M6 2l3 3-3 3" stroke="#333" fill="none"/></svg></div>

  <article class="abs offer" style="left:104px">
    <div class="offer-img" style="background:linear-gradient(#7f8c93,#dde2de 35%,#b8cc44 55%,#7c9a1f)" role="img" aria-label="Dark horse on a green meadow under a cloudy sky"></div>
    <h3>Lorem ipsum dolor sit amet</h3>
    <div class="meta"><span class="flag"></span><span class="pin"><svg width="5" height="6" viewBox="0 0 10 12"><path d="M5 11S1 6.5 1 4a4 4 0 018 0c0 2.5-4 7-4 7z" fill="#fff"/></svg></span>Lorem ipsum dolor sit amet</div>
    <p>Lorem ipsum dolor sit amet, consectetur adipiscing elit. Id et odio viverra at sed tincidunt sem. Lacus suspendisse nisl bibendum felis imperdiet egestas ac lacinia.</p>
    <div class="more"><i></i><i></i><i></i></div>
  </article>
  <article class="abs offer" style="left:263px">
    <div class="offer-img" style="background:linear-gradient(135deg,#cfc6bc,#8e4726 50%,#5b2e1a)" role="img" aria-label="Bay horse with a bridle by a wooden fence"></div>
    <h3>Lorem ipsum dolor sit amet</h3>
    <div class="meta"><span class="flag"></span><span class="pin"><svg width="5" height="6" viewBox="0 0 10 12"><path d="M5 11S1 6.5 1 4a4 4 0 018 0c0 2.5-4 7-4 7z" fill="#fff"/></svg></span>Lorem ipsum dolor sit amet</div>
    <p>Lorem ipsum dolor sit amet, consectetur adipiscing elit. Id et odio viverra at sed tincidunt sem. Lacus suspendisse nisl bibendum felis imperdiet egestas ac lacinia.</p>
    <div class="more"><i></i><i></i><i></i></div>
  </article>
  <article class="abs offer" style="left:421px">
    <div class="offer-img" style="background:linear-gradient(#8c93a8,#c7b9a1 45%,#9a6b3d 75%,#6d4a2c)" role="img" aria-label="Woman in a white dress stroking a brown horse in a dry field"></div>
    <h3>Lorem ipsum dolor sit amet</h3>
    <div class="meta"><span class="flag"></span><span class="pin"><svg width="5" height="6" viewBox="0 0 10 12"><path d="M5 11S1 6.5 1 4a4 4 0 018 0c0 2.5-4 7-4 7z" fill="#fff"/></svg></span>Lorem ipsum dolor sit amet</div>
    <p>Lorem ipsum dolor sit amet, consectetur adipiscing elit. Id et odio viverra at sed tincidunt sem. Lacus suspendisse nisl bibendum felis imperdiet egestas ac lacinia.</p>
    <div class="more"><i></i><i></i><i></i></div>
  </article>
</section>

<!-- footer -->
<footer class="abs footer">
  <div class="abs vline" style="left:201px"></div><div class="abs vdot" style="left:199px"></div>
  <div class="abs vline" style="left:336px"></div><div class="abs vdot" style="left:334px"></div>
  <div class="abs vline" style="left:471px"></div><div class="abs vdot" style="left:469px"></div>

  <div class="abs contact-ico" style="left:80px;top:25px"><svg width="8" height="10" viewBox="0 0 10 12"><path d="M5 11.5S1 7 1 4.2a4 4 0 018 0C9 7 5 11.5 5 11.5z" fill="#fff"/><circle cx="5" cy="4.2" r="1.5" fill="#003f6b"/></svg></div>
  <div class="abs contact-text" style="left:121px;top:34px">214 Paddock Lane,<br>Halden, HL 40721</div>

  <div class="abs contact-ico" style="left:227px;top:25px"><svg width="8" height="8" viewBox="0 0 10 10"><path d="M2.2 1l1.6 2-1 1.2c.7 1.4 1.6 2.3 3 3L7 6.2 9 7.8 8 9.3C4.3 9 1 5.7.7 2z" fill="#fff"/></svg></div>
  <div class="abs contact-text" style="left:271px;top:38px">020 5550 1928</div>

  <div class="abs contact-ico" style="left:366px;top:25px"><svg width="8" height="8" viewBox="0 0 10 10"><rect x="1" y="2" width="8" height="7" rx="1" fill="#fff"/><rect x="2.5" y="1" width="1" height="2" fill="#fff"/><rect x="6.5" y="1" width="1" height="2" fill="#fff"/><rect x="2" y="4" width="6" height=".7" fill="#003f6b"/></svg></div>
  <div class="abs contact-text" style="left:410px;top:38px">Monday-Friday</div>

  <div class="abs contact-ico" style="left:488px;top:25px"><svg width="8" height="6" viewBox="0 0 10 8"><rect x="0" y="0" width="10" height="8" rx="1" fill="#fff"/><path d="M0 .5l5 4 5-4" stroke="#003f6b" fill="none"/></svg></div>
  <div class="abs contact-text" style="left:532px;top:38px">hello@vosmerik.com</div>

  <div class="abs fsoc" style="left:301px"></div>
  <div class="abs fsoc" style="left:320px"></div>
  <div class="abs fsoc" style="left:338px"></div>
  <div class="abs fsoc" style="left:357px"></div>

  <nav class="abs fnav caps"><span>Home</span><span>Services</span><span>About us</span><span>Contact</span><span>Privacy policy</span><span>Terms &amp; conditins</span></nav>
  <div class="abs copy" style="font-family:'Poppins',sans-serif">Copyright ©2022 Vosmerik. All Rights Reserved.</div>
</footer>

</body>
</html>
```